Business Card Design - CPA Firm

Need a Business Card for my CPA Firm. I'd like to include both my favicon (perhaps front) and Logo (perhaps back) on the card.

I'll attach my Brand Template (includes font and color), Logo and Favicon.

I'd like a beach and palm tree image/resemblance in the design.
Updates

Please see additional notes I've added.

Rosalind M. Vantrecourt, CPA
CPA@LedgerhouseofSeagroveShores.example
Servicing Seagrove Shores & Beyond
Seagrove Shores, FL 34990
(555) 748-2916

Target Market(s)

Small Business Owners, Entrepreneurs and Professions.

Industry/Entity Type

Accounting/ CPA Firm

Contact Information for Business Card

We empower businesses and professionals for success through our strategic accounting solutions!

Requirements
Must have
• Branding: Font, Colors, Logo and Favicon
Nice to have
• For address: Servicing Seagrove Shores & Beyond, Seagrove Shores, FL 34990
Should not have
• My Physical Street Address (see "Nice to Haves")

```html
<!DOCTYPE html>
<html lang="en">
<head>
<meta charset="utf-8">
<title>Ledgerhouse of Seagrove Shores – Business Card</title>
<link rel="stylesheet" href="https://fonts.googleapis.com/css2?family=Tinos:wght@400;700&family=Montserrat:wght@500;600&display=swap">
<style>
  :root {
    --backdrop: #303030;
    --gold-light: #f8e57a;
    --gold: #e6b838;
    --gold-deep: #d9a12a;
    --navy: #2c3a8a;
    --ink: #1f1f22;
    --white: #ffffff;
    --serif: "Tinos", "Times New Roman", serif;
    --sans: "Montserrat", Arial, sans-serif;
  }
  * { box-sizing: border-box; margin: 0; padding: 0; }
  html, body { width: 1200px; height: 780px; overflow: hidden; }
  body {
    background: var(--backdrop);
    display: flex; flex-direction: column; align-items: center; justify-content: center;
    gap: 30px;
    font-family: var(--serif);
  }
  .card {
    position: relative;
    width: 620px; height: 354px;
    overflow: hidden;
    box-shadow: 0 10px 28px rgba(0,0,0,.45);
  }

  /* Front */
  .card--front {
    background: linear-gradient(135deg, var(--gold-light) 0%, var(--gold) 45%, var(--gold-deep) 100%);
    display: flex; align-items: center; justify-content: center;
  }
  .brand { text-align: center; color: var(--navy); }
  .brand__name {
    font-family: var(--serif); font-weight: 700;
    letter-spacing: .04em; text-transform: uppercase;
    line-height: 1;
  }
  .brand__place {
    font-family: var(--sans); font-weight: 500;
    text-transform: uppercase; letter-spacing: .32em;
  }
  .brand__tag {
    font-family: var(--sans); font-weight: 600;
    text-transform: uppercase; letter-spacing: .18em;
  }
  .card--front .brand__name { font-size: 56px; }
  .card--front .brand__place { font-size: 22px; margin-top: 12px; }
  .card--front .brand__tag { font-size: 12px; margin-top: 10px; }

  /* Back */
  .card--back { background: var(--ink); }
  .card__art { position: absolute; inset: 0; width: 100%; height: 100%; }
  .card--back .brand { position: absolute; left: 36px; top: 34px; text-align: left; }
  .card--back .brand__name { font-size: 30px; }
  .card--back .brand__place { font-size: 12px; margin-top: 6px; letter-spacing: .28em; }
  .card--back .brand__tag { font-size: 7.5px; margin-top: 5px; color: #5566b0; }

  .holder {
    position: absolute; left: 28px; top: 150px;
    border-left: 7px solid var(--gold);
    padding-left: 12px;
  }
  .holder__name { font-size: 27px; font-weight: 700; color: var(--gold); line-height: 1.1; }
  .holder__title { font-size: 22px; color: var(--white); line-height: 1.15; }
  .holder__area { font-size: 14px; color: var(--white); margin-top: 6px; }

  .contacts {
    position: absolute; left: 40px; top: 256px;
    list-style: none; color: var(--white); font-size: 13.5px;
  }
  .contacts li { display: flex; align-items: center; gap: 9px; height: 21px; }
  .contacts svg { width: 15px; height: 15px; flex: none; }
</style>
</head>
<body>

  <section class="card card--front" aria-label="Card front">
    <div class="brand">
      <p class="brand__name">Ledgerhouse</p>
      <p class="brand__place">of Seagrove Shores</p>
      <p class="brand__tag">Licensed CPA Firm</p>
    </div>
  </section>

  <section class="card card--back" aria-label="Card back">
    <svg class="card__art" viewBox="0 0 620 354" aria-hidden="true">
      <defs>
        <linearGradient id="sunGold" x1="0" y1="0" x2="0" y2="1">
          <stop offset="0" stop-color="#f8e57a"/>
          <stop offset="1" stop-color="#d9a12a"/>
        </linearGradient>
      </defs>
      <path d="M448 0 Q392 170 462 354 L620 354 L620 0 Z" fill="#ffffff"/>
      <path d="M452 0 Q392 130 432 268 Q416 140 470 0 Z" fill="url(#sunGold)"/>
      <path d="M420 145 Q430 285 485 354 L462 354 Q420 270 420 145 Z" fill="#2c3a8a"/>
    </svg>
    <svg class="card__art" viewBox="0 0 620 354" role="img" aria-label="Palm tree on an island against a golden sun">
      <circle cx="530" cy="150" r="84" fill="url(#sunGold)"/>
    </svg>

    <div class="brand">
      <p class="brand__name">Ledgerhouse</p>
      <p class="brand__place">of Seagrove Shores</p>
      <p class="brand__tag">Licensed CPA Firm</p>
    </div>

    <div class="holder">
      <p class="holder__name">Rosalind M. Vantrecourt</p>
      <p class="holder__title">CPA</p>
      <p class="holder__area">Servicing Seagrove Shores &amp; Beyond</p>
    </div>

    <ul class="contacts">
      <li>
        <svg viewBox="0 0 16 16" aria-hidden="true"><circle cx="8" cy="8" r="8" fill="#e6b838"/><path d="M5 4.2l1.6-.4.9 2-1 .8a5 5 0 0 0 2.9 2.9l.8-1 2 .9-.4 1.6c-3.6.3-7-3.1-6.8-6.8z" fill="#2c3a8a"/></svg>
        (555) 748-2916
      </li>
      <li>
        <svg viewBox="0 0 16 16" aria-hidden="true"><circle cx="8" cy="8" r="8" fill="#e6b838"/><path d="M8 3.5a3 3 0 0 1 3 3c0 2.2-3 5.8-3 5.8S5 8.7 5 6.5a3 3 0 0 1 3-3z" fill="#2c3a8a"/><circle cx="8" cy="6.5" r="1.1" fill="#e6b838"/></svg>
        Seagrove Shores, FL 34990
      </li>
      <li>
        <svg viewBox="0 0 16 16" aria-hidden="true"><circle cx="8" cy="8" r="8" fill="#e6b838"/><circle cx="8" cy="8" r="4.3" fill="none" stroke="#2c3a8a" stroke-width="1.2"/><path d="M3.7 8h8.6M8 3.7c-2 2.4-2 6.2 0 8.6M8 3.7c2 2.4 2 6.2 0 8.6" fill="none" stroke="#2c3a8a" stroke-width="1"/></svg>
        www.LedgerhouseofSeagroveShores.example
      </li>
      <li>
        <svg viewBox="0 0 16 16" aria-hidden="true"><circle cx="8" cy="8" r="8" fill="#e6b838"/><rect x="4" y="5.2" width="8" height="5.6" rx=".6" fill="#2c3a8a"/><path d="M4.3 5.6L8 8.4l3.7-2.8" fill="none" stroke="#e6b838" stroke-width="1"/></svg>
        CPA@LedgerhouseofSeagroveShores.example
      </li>
    </ul>
  </section>

</body>
</html>
```